Brellin Vale , Australian natural body care needs a new product label.

I have just had a logo designed by sketchharbor and now want this logo added to a product label design. The product is a cleansing, moisturising hand scrub with only natural ingredients and anti microbial essential oils. I have made this product for over 15 years and it needs a new more appropriate image. It was previously called morning ritual and came in a tube. the new packaging is a white pump pack container. Dimensions for the label are 185mm wide and 80mm high, I have attached a sheet with all of the information required on the label.
Updates

Target Market(s)

anyone with dry skin

Industry/Entity Type

Cosmetics

Requirements
Must have
• professional and upmarket appearance. Be creative and surprise me your take on how this label should look.
Nice to have
• Natural colours, the attached logo should be changed in colour to match the label.

```html
<!DOCTYPE html>
<html lang="en">
<head>
<meta charset="utf-8">
<title>Brellin Vale Hand Scrub Label</title>
<link href="https://fonts.googleapis.com/css2?family=Open+Sans:ital,wght@0,400;0,600;0,700;1,700&family=Raleway:wght@400&display=swap" rel="stylesheet">
<style>
  :root {
    --backdrop: #dcdcdc;
    --label-white: #fbfbfb;
    --pack-blue: #3fc3ee;
    --pack-blue-deep: #22a9dd;
    --silver: #c9c9c9;
    --leaf-green: #9acb4e;
    --leaf-green-deep: #5f9a24;
    --leaf-green-light: #c2e08f;
    --ink: #4a4a4a;
    --ink-soft: #5c5c5c;
    --brand-blue: #2db4e6;
  }
  * { margin: 0; padding: 0; box-sizing: border-box; }
  html, body {
    width: 1075px; height: 1200px; overflow: hidden;
    background: var(--backdrop);
  }
  .canvas {
    position: relative; width: 1075px; height: 1200px;
    display: flex; align-items: center; justify-content: center;
  }
  .label {
    position: relative; width: 440px; height: 1060px;
    background: var(--label-white);
    box-shadow: 0 18px 40px rgba(0,0,0,0.12);
    overflow: hidden;
    font-family: "Raleway", sans-serif;
    color: var(--ink);
  }
  .label__cap-band {
    height: 150px;
    background: linear-gradient(90deg, var(--pack-blue-deep), var(--pack-blue) 45%, #6ad4f4 60%, var(--pack-blue));
  }
  .label__silver-rule {
    height: 14px;
    background: linear-gradient(180deg, #e9e9e9, var(--silver) 50%, #f2f2f2);
  }
  .label__leaf-wash {
    position: absolute; left: 0; top: 600px; width: 110px; height: 380px;
    background: linear-gradient(160deg, rgba(210,210,210,0.0), rgba(205,205,205,0.55) 50%, rgba(230,230,230,0.0));
    border-radius: 0 80px 80px 0;
  }
  .brand {
    margin-top: 90px;
    display: flex; align-items: center; justify-content: center; gap: 12px;
  }
  .brand__dot {
    width: 26px; height: 26px; border-radius: 50%;
    background: var(--brand-blue);
  }
  .brand__name {
    font-family: "Open Sans", sans-serif; font-weight: 600;
    font-size: 44px; color: var(--brand-blue); letter-spacing: 0.5px;
  }
  .product-line {
    margin-top: 30px; text-align: center;
    font-family: "Open Sans", sans-serif; font-weight: 700; font-style: italic;
    font-size: 19px; color: var(--ink-soft);
  }
  .product-name {
    position: relative; margin: 26px auto 0; width: 380px; height: 150px;
    border-radius: 26px 40px 30px 46px;
    background: linear-gradient(90deg, var(--leaf-green-deep), var(--leaf-green-light) 45%, var(--leaf-green) 100%);
    display: flex; align-items: center; justify-content: center;
  }
  .product-name__title {
    font-family: "Open Sans", sans-serif; font-weight: 700; font-style: italic;
    font-size: 56px; color: #ffffff; letter-spacing: 0.5px;
  }
  .benefits {
    margin-top: 26px; text-align: center;
    font-size: 19px; line-height: 1.3; color: var(--ink-soft);
  }
  .benefits__rule {
    width: 280px; height: 1px; margin: 16px auto;
    background: var(--ink);
  }
  .natural-seal {
    position: absolute; left: 130px; top: 800px;
    width: 120px; height: 100px;
  }
  .origin {
    position: absolute; left: 0; right: 0; bottom: 46px;
    text-align: center; font-size: 17px; color: var(--ink-soft);
  }
  .net-weight {
    position: absolute; right: 0; bottom: 0;
    width: 100px; height: 40px;
    background: var(--pack-blue);
    color: #ffffff; font-size: 14px; font-style: italic;
    display: flex; align-items: center; justify-content: center;
  }
</style>
</head>
<body>
  <div class="canvas">
    <section class="label">
      <div class="label__cap-band"></div>
      <div class="label__silver-rule"></div>
      <div class="label__leaf-wash" role="img" aria-label="Faint pale grey leaf motif"></div>

      <div class="brand">
        <span class="brand__dot"></span>
        <span class="brand__name">Brellin Vale</span>
      </div>

      <p class="product-line">Cleansing &amp; Moisturising</p>

      <div class="product-name" role="img" aria-label="Green brush stroke behind the product name">
        <h1 class="product-name__title">Hand Scrub</h1>
      </div>

      <div class="benefits">
        <p>Dry &amp; Damaged Hand Repair<br>Immediate results</p>
        <div class="benefits__rule"></div>
        <p>Ultra-moisturising with<br>Rosehip &amp; essential oil</p>
      </div>

      <svg class="natural-seal" viewBox="0 0 120 100" aria-label="Natural ingredients seal">
        <circle cx="60" cy="50" r="44" fill="none" stroke="var(--leaf-green)" stroke-width="3"/>
      </svg>

      <p class="origin">Made in Australia</p>
      <div class="net-weight">250gm</div>
    </section>
  </div>
</body>
</html>
```